Bright Harbor Works Buisness Cards

Provide a business card layout

Paul Wexford
PO Box 742
Alder Falls 02318
paul@thwexample.com

Industry/Entity Type

Business

Font styles to use
Serif

Colors
f04a50

```html
<!DOCTYPE html>
<html lang="en">
<head>
<meta charset="utf-8">
<title>Bright Harbor Works Business Cards</title>
<link rel="stylesheet" href="https://fonts.googleapis.com/css2?family=Cinzel:wght@600&family=Lato:wght@400;700&display=swap">
<style>
  :root {
    --page: #ece8e2;
    --paper: #ffffff;
    --red: #b3191f;
    --red-dark: #9a1217;
    --gold: #eba93b;
    --gold-light: #f4c25c;
    --ink: #1c1c1c;
    --muted-line: #f7f3ec;
  }
  * { margin: 0; padding: 0; box-sizing: border-box; }
  html, body { width: 1200px; height: 1000px; overflow: hidden; }
  body {
    background: var(--page);
    font-family: "Lato", sans-serif;
    position: relative;
  }
  .card {
    position: absolute;
    left: 285px;
    width: 630px;
    height: 360px;
    background: var(--paper);
    overflow: hidden;
    box-shadow: 0 6px 18px rgba(0,0,0,0.18);
  }
  .card--back { top: 80px; }
  .card--front { top: 540px; }

  /* Back */
  .back__band {
    position: absolute; left: 0; width: 100%;
    background: linear-gradient(90deg, var(--gold-light), var(--gold));
  }
  .back__band--top { top: 0; height: 58px; }
  .back__band--bottom { bottom: 0; height: 58px; }
  .brand {
    display: flex; align-items: center; gap: 14px;
    font-family: "Cinzel", serif; font-weight: 600; color: var(--ink);
    white-space: nowrap;
  }
  .brand__dot {
    border-radius: 50%;
    background: var(--red);
    flex: none;
  }
  .back__brand {
    position: absolute; left: 0; right: 0; top: 150px;
    justify-content: center; font-size: 40px;
  }
  .back__brand .brand__dot { width: 34px; height: 34px; }

  /* Front */
  .front__brand {
    position: absolute; right: 50px; top: 48px; font-size: 26px;
  }
  .front__brand .brand__dot { width: 24px; height: 24px; }
  .front__panel {
    position: absolute; left: 0; top: 120px; width: 100%; height: 168px;
    background: linear-gradient(100deg, var(--red-dark), var(--red) 55%, var(--red-dark));
    color: var(--paper);
  }
  .contact {
    position: absolute; left: 34px; top: 18px;
    list-style: none; font-size: 13px; line-height: 1.3;
  }
  .contact__item { display: flex; gap: 12px; margin-bottom: 9px; }
  .contact__icon { width: 20px; height: 20px; flex: none; }
  .person {
    position: absolute; right: 50px; top: 70px;
    font-size: 22px; letter-spacing: 0.5px; text-transform: uppercase;
  }
  .person__first { font-weight: 700; }
  .person__last { font-weight: 400; }
  .license {
    position: absolute; left: 170px; bottom: 8px;
    font-size: 12px; color: var(--gold-light);
  }
  .front__rule {
    position: absolute; left: 0; top: 288px; width: 100%; height: 10px;
    background: var(--muted-line);
  }
  .front__band {
    position: absolute; left: 0; bottom: 0; width: 100%; height: 62px;
    background: linear-gradient(90deg, var(--gold-light), var(--gold));
  }
</style>
</head>
<body>
  <section class="card card--back">
    <div class="back__band back__band--top"></div>
    <div class="brand back__brand"><span class="brand__dot"></span>Bright Harbor Works</div>
    <div class="back__band back__band--bottom"></div>
  </section>

  <section class="card card--front">
    <div class="brand front__brand"><span class="brand__dot"></span>Bright Harbor Works</div>
    <div class="front__panel">
      <ul class="contact">
        <li class="contact__item">
          <svg class="contact__icon" viewBox="0 0 20 20" fill="none" stroke="#fff" stroke-width="1.5"><rect x="6" y="2" width="8" height="16" rx="1.5"/><line x1="9" y1="15" x2="11" y2="15"/></svg>
          <span>555 014 2290</span>
        </li>
        <li class="contact__item">
          <svg class="contact__icon" viewBox="0 0 20 20" fill="none" stroke="#fff" stroke-width="1.3"><circle cx="10" cy="10" r="8"/><ellipse cx="10" cy="10" rx="3.5" ry="8"/><line x1="2" y1="10" x2="18" y2="10"/></svg>
          <span>paul@thwexample.com<br>www.thwexample.com</span>
        </li>
        <li class="contact__item">
          <svg class="contact__icon" viewBox="0 0 20 20" fill="none" stroke="#fff" stroke-width="1.5"><rect x="2" y="5" width="16" height="11"/><polyline points="2,5 10,11 18,5"/></svg>
          <span>PO Box 742<br>Alder Falls 02318</span>
        </li>
      </ul>
      <p class="person"><span class="person__first">Paul</span> <span class="person__last">Wexford</span></p>
      <p class="license">Builders License CS 048215</p>
    </div>
    <div class="front__rule"></div>
    <div class="front__band"></div>
  </section>
</body>
</html>
```